Media Kit

We're a editorial website that enjoys some love from advertisers and publicists.
We need a digital media kit (probably in PDF form) that tells a story about who we are, who our readers are, our traffic and so forth.
The copy and a logo file are attached - you just need to make it look awesome. Our logo font is 'elephant'. Our secondary font is Futura Lt Bt.
To get a sense of the types of media kits in the market, check out:
http://www.korvanpresskit.example/hotdata/publishers/korvpk/advertiser/5094712/6473920/MediaKitFinal_2013.pdf
http://www.moswellhaus.example/static/corporate/images/4a91e2/corporate/assets/mh_mediakit.pdf
Or look to other traditional and digital magazines in the lifestyle space.
Please note: we will require the original artwork files from the successful designer.
Updates
If you wish, a sample rather than the whole project is fine to secure payment.
Target Market(s)
Publicists, Marketing Managers, Media Buyers
Industry/Entity Type
Digital
Look and feel
Each slider illustrates characteristics of the customer's brand and the style your logo design should communicate.

```html
<!DOCTYPE html>
<html lang="en">
<head>
<meta charset="utf-8">
<title>Hollis Row — Media Kit</title>
<link rel="stylesheet" href="https://fonts.googleapis.com/css2?family=Jost:wght@300;400&display=swap">
<style>
:root{
  --stage:#2e2e2e;
  --paper:#ffffff;
  --ink:#1c1c1c;
  --taupe:#8b7e76;
  --mute:#c9c3bf;
  --photo-a:#ece9e6;
  --photo-b:#d6d1cc;
}
*{margin:0;padding:0;box-sizing:border-box}
html,body{width:1200px;height:1000px;overflow:hidden;background:var(--stage)}
body{position:relative;font-family:"Jost",sans-serif;font-weight:300;color:var(--ink)}
.page{position:absolute;width:500px;height:353px;background:var(--paper);overflow:hidden}
.page--cover{left:60px;top:120px}
.page--about{left:648px;top:120px}
.page--stats{left:60px;top:547px}
.page--network{left:648px;top:547px}
.abs{position:absolute}

.brand{position:absolute;left:26px;top:32px;display:flex;align-items:center;gap:5px}
.brand__dot{width:14px;height:14px;border-radius:50%;background:var(--ink)}
.brand__name{font-size:11px;font-weight:400;color:var(--ink);letter-spacing:.3px}

.heading{position:absolute;left:206px;font-size:18px;font-weight:300;color:var(--ink)}
.copy{position:absolute;left:206px;width:272px;font-size:7.4px;line-height:9.4px;color:var(--taupe)}
.copy p{margin-bottom:5.6px}

/* cover */
.cover__photo{position:absolute;inset:0;background:linear-gradient(160deg,var(--photo-a),var(--photo-b))}
.cover__label{position:absolute;left:143px;top:202px;width:272px;height:48px;background:rgba(255,255,255,.88);display:flex;align-items:center;padding:0 12px;box-shadow:0 2px 4px rgba(0,0,0,.12)}
.cover__label .brand{position:static}
.cover__title{margin-left:auto;text-align:right;line-height:17px}
.cover__title .sub{font-size:13px;color:var(--taupe)}
.cover__title .main{font-size:17px;color:var(--ink)}

/* about */
.vision__title{left:26px;top:177px;font-size:17px}
.vision__text{left:26px;top:208px;width:110px;font-size:15px;line-height:19px;color:var(--taupe)}

/* stats */
.stats__lede{top:50px;width:300px;font-size:8px;line-height:10px}
.stat-label{font-size:7px;text-align:center;color:var(--ink)}
.returning{left:170px;top:255px;width:90px;text-align:center;color:var(--ink)}
.returning .big{font-size:19px;line-height:20px}
.returning .sm{font-size:7px;line-height:8px}
.returning .mid{font-size:11px;line-height:13px}

/* network */
.partners{top:80px;display:grid;grid-template-columns:85px 85px;font-size:7.4px;line-height:9.4px;color:var(--taupe)}
.plans{top:160px;list-style:none;font-size:7.4px;line-height:9.4px;color:var(--taupe);width:270px}
.plans li{padding-left:10px;position:relative;margin-bottom:4px}
.plans li::before{content:">";position:absolute;left:0}
.contact__title{left:26px;top:242px;font-size:17px}
.contact__text{left:26px;top:272px;font-size:7.4px;line-height:9.4px;color:var(--taupe)}
</style>
</head>
<body>

<section class="page page--cover">
  <div class="cover__photo" role="img" aria-label="Studio group photo of five friends in autumn fashion, one holding a small dog"></div>
  <div class="cover__label">
    <div class="brand"><span class="brand__dot"></span><span class="brand__name">Hollis Row</span></div>
    <div class="cover__title"><div class="sub">hollis row</div><div class="main">media kit</div></div>
  </div>
</section>

<section class="page page--about">
  <div class="brand"><span class="brand__dot"></span><span class="brand__name">Hollis Row</span></div>
  <h2 class="heading" style="top:22px">Who Are We?</h2>
  <div class="copy" style="top:52px">
    <p>Hollis Row is all about the lovely things in life.</p>
    <p>It is the home for delectable fashion, enviable interiors, inspired music and memorable travel experiences to name just a few.</p>
    <p>Most of all however, it’s about these things being accessible to everyone.</p>
    <p>That means that as beautiful as the photos look, we know most people can’t really live with all white interiors. Or walk down the street wearing a nude tulle skirt.</p>
    <p>That said, there’s no reason practicality means boring or ugly.</p>
    <p>Of course, like real lives, wardrobes, diets and MP3 players, at Hollis Row Verlaine lives happily alongside Kestrel, you’ll see superfoods as well as sundaes and hear Mira Solace on the same playlist as Dusty Harlow.</p>
    <p>Hollis Row is based in Melbourne, Australia and takes submissions and content from all over the world.</p>
    <p>With everything we do we always consider the fact that we live in an age where people see, read, hear and experience things that might be happening in the next street or on the other side of the world.</p>
    <p>This means that everything that appears in Hollis Row is meaningful no matter where you live, work and play.</p>
  </div>
  <h2 class="abs vision__title">Our Vision</h2>
  <p class="abs vision__text">The home of accessible, inspiring and beautiful lifestyle elements.</p>
</section>

<section class="page page--stats">
  <div class="brand"><span class="brand__dot"></span><span class="brand__name">Hollis Row</span></div>
  <h2 class="heading" style="top:22px">The Picture</h2>
  <p class="copy stats__lede">Hollis Row is very young, but we’re growing up fast.<br>Our readership and reach expands every day.</p>
  <svg class="abs" style="left:0;top:0" width="500" height="353" viewBox="0 0 500 353" font-family="Jost, sans-serif">
    <!-- visitors -->
    <circle cx="95" cy="170" r="62" fill="var(--mute)"/>
    <circle cx="95" cy="170" r="33" fill="var(--ink)"/>
    <text x="95" y="160" fill="#fff" font-size="7" text-anchor="middle">Up to</text>
    <text x="95" y="173" fill="#fff" font-size="12" text-anchor="middle">3,500</text>
    <text x="95" y="182" fill="#fff" font-size="6" text-anchor="middle">unique visitors</text>
    <text x="95" y="190" fill="#fff" font-size="6" text-anchor="middle">each day</text>
    <!-- time on site -->
    <text x="240" y="142" font-size="7" text-anchor="middle" fill="var(--ink)">Average time on site</text>
    <rect x="180" y="147" width="120" height="55" rx="6" fill="#3a3a3a"/>
    <rect x="186" y="153" width="108" height="43" rx="3" fill="#d9d6d3"/>
    <text x="240" y="186" font-size="30" text-anchor="middle" fill="var(--ink)" letter-spacing="3">04:30</text>
    <!-- pages per visit -->
    <rect x="335" y="112" width="128" height="80" rx="6" fill="none" stroke="var(--ink)" stroke-width="5"/>
    <rect x="325" y="192" width="150" height="6" fill="var(--ink)"/>
    <text x="399" y="133" font-size="7" text-anchor="middle" fill="var(--ink)">Average pages per visit</text>
    <text x="399" y="168" font-size="24" text-anchor="middle" fill="var(--ink)">7.3</text>
    <!-- returning -->
    <circle cx="130" cy="285" r="27" fill="var(--ink)"/>
    <path d="M113 279h18v-9l15 15-15 15v-9h-18z" fill="#fff"/>
    <!-- first time donut -->
    <circle cx="350" cy="268" r="45" fill="none" stroke="var(--mute)" stroke-width="18"/>
    <path d="M350 223 A45 45 0 1 0 365 310" fill="none" stroke="var(--ink)" stroke-width="18"/>
    <text x="350" y="260" font-size="6.5" text-anchor="middle" fill="var(--ink)">More than half</text>
    <text x="350" y="269" font-size="6.5" text-anchor="middle" fill="var(--ink)">our traffic is made up</text>
    <text x="350" y="278" font-size="6.5" text-anchor="middle" fill="var(--ink)">of first time visitors</text>
  </svg>
  <div class="abs returning">
    <div class="big">38%</div>
    <div class="sm">of readers<br>come back</div>
    <div class="mid">3 or more times</div>
    <div class="sm">a month</div>
  </div>
</section>

<section class="page page--network">
  <div class="brand"><span class="brand__dot"></span><span class="brand__name">Hollis Row</span></div>
  <h2 class="heading" style="top:22px">Our Network</h2>
  <p class="copy" style="top:50px">Some of our current and previous advertisers and affiliate partners include:</p>
  <div class="abs partners" style="left:206px">
    <span>The Rackhouse</span><span>Cove Beauty</span>
    <span>Closet Nine</span><span>Ashgrove</span>
    <span>Pairwise Fashion</span><span>Leon Marchetti</span>
  </div>
  <h2 class="heading" style="top:128px">The Year Ahead</h2>
  <ul class="abs plans" style="left:206px">
    <li>Establishment of contributor network to have daily updates in each major category.</li>
    <li>Launch our weekly newsletter.</li>
    <li>Develop custom visual content.</li>
  </ul>
  <h2 class="abs contact__title">Contact</h2>
  <div class="abs contact__text">
    <p style="margin-bottom:9px">Press Releases &amp; Other Media Enquiries</p>
    <p>Clara Whitfield<br>clara@hollisrow.example<br>+61 (0) 400 000 123<br>www.hollisrow.example</p>
  </div>
</section>

</body>
</html>
```